TILLvanta (www.tillvanta.example) needs exciting professional Business Cards

TILLvanta is an exciting new start-up targeting innovative ways to engage with retail customers at the point of sale.
Our Vision
Through applying new thinking to an old business we are reinventing selected segments of the Australian retail messaging industry, generating significant value for our customers, our suppliers, and our owners.
We operate with integrity, agility, and intelligence to doing things smarter, faster and more efficiently.
We bring deep industry expertise, deep relationships with customers and suppliers, and a will to see the old ways give way to smarter ways – this is why we win.
From this economically sustainable platform, we will examine the disruption of other market segments by further leveraging the elements that make us successful.
Our Values
With our clients, with our suppliers, with our staff, and with our owners:
# We Partner – We align the interest of all stakeholders by striving to ensure everything we do is mutually beneficial and commercially sustainable in the long term. We are clear with all our stakeholders about what our expectations are of them, and we seek clarity from them in their expectations of us.
# We Innovate – In the segments we choose to compete in, we bring fresh ideas, new business processes, the right relationships, and the right technology to ensure the supply chain is nimble, competitive, and reliable.
# We are Accountable – We say what we will do, and then do what we say.
# We Perform – We use our skills, relationships, and reputation to deliver value to our customers, suppliers, and owners.
Initially we are building our business from low-tech through printing promotional offers and retailer messages on ATM and EFTPOS receipts, but as soon as cash flow supports it we will be engaging in high-tech real-time targeted offers to the specific consumer.
I'd like the cards to reflect our values.
Please check out the web site we have just launched - it is pretty basic but it has only been up a week. We intend to sharpen it over the coming weeks, but you'll get the idea of what our core messages are.
I have recently sourced a logo from MarkForge, and have attached the source files for use.
Personal information to include:
Name: FirstName Surname
Title: Managing Director
email: first.surname@tillvanta.example
Mobile: +61-427-318-654
Generic Co Details to include:
Web: www.tillvanta.example
email: tillvanta@tillvanta.example
Fax: +61-8-7394-2816
Offices & Agents: Harbourton, Kellmere, Ashgrove, Denley, Marrow Bay
Byline: Innovation . Integrity . Service
Target Market(s)
Our customers are large corporations that have professional Point Of Sale marketing experts looking for a supplier with an edge over others in a crowded market. The buyer of our product and services is ultimately a communications expert.
They want to see distinctive competence, and an agility of thinking that will make them money through driving more consumer spending.
Industry/Entity Type
Retail
Look and feel
Each slider illustrates characteristics of the customer's brand and the style your logo design should communicate.

```html
<!DOCTYPE html>
<html lang="en">
<head>
<meta charset="utf-8">
<title>Tillvanta Business Cards</title>
<link href="https://fonts.googleapis.com/css2?family=Open+Sans:wght@400;600;700&display=swap" rel="stylesheet">
<style>
  :root {
    --page-bg: #e4e4e5;
    --card-white: #ffffff;
    --brand-blue: #1a80c9;
    --slate: #58595b;
    --text-light: #f2f2f2;
    --mark-grey: #e6e6e6;
  }
  * { margin: 0; padding: 0; box-sizing: border-box; }
  html, body {
    width: 1200px; height: 999px; overflow: hidden;
    background: var(--page-bg);
    font-family: "Open Sans", Arial, sans-serif;
  }
  .card {
    position: absolute;
    width: 500px; height: 286px;
    box-shadow: 0 6px 18px rgba(0,0,0,0.18);
    overflow: hidden;
  }
  .brand-name { position: absolute; font-weight: 600; line-height: 1; white-space: nowrap; }

  /* Front */
  .card-front { left: 70px; top: 250px; background: var(--card-white); }
  .front-header { position: absolute; left: 0; top: 0; width: 100%; height: 118px; background: var(--card-white); }
  .card-front .brand-name { left: 130px; top: 38px; font-size: 44px; color: var(--brand-blue); }
  .accent-line { position: absolute; left: 0; top: 118px; width: 100%; height: 6px; background: var(--brand-blue); }
  .info-panel { position: absolute; left: 0; top: 124px; width: 100%; height: 136px; background: var(--slate); color: var(--text-light); }
  .notch { position: absolute; left: 30px; top: -6px; width: 0; height: 0;
    border-left: 7px solid transparent; border-right: 7px solid transparent; border-bottom: 7px solid var(--slate); }
  .footer-band { position: absolute; left: 0; top: 260px; width: 100%; height: 16px; background: var(--brand-blue); }
  .person { position: absolute; left: 30px; top: 18px; }
  .person-name { font-size: 17px; font-weight: 700; }
  .person-title { font-size: 11.5px; margin-top: 1px; }
  .contact-list { list-style: none; font-size: 11.5px; }
  .contact-list li { display: flex; align-items: center; gap: 8px; height: 17px; white-space: nowrap; }
  .contact-list svg { width: 14px; height: 12px; flex: none; }
  .person .contact-list { margin-top: 26px; }
  .company { position: absolute; left: 262px; top: 12px; }
  .company-heading { font-size: 11.5px; font-weight: 700; }
  .company-cities { font-size: 11.5px; line-height: 15px; margin-bottom: 8px; }
  .company .contact-list li { gap: 6px; }
  .sep { margin-right: 2px; }

  /* Back */
  .card-back { left: 630px; top: 470px; background: var(--slate); }
  .card-back .brand-name { left: 100px; top: 106px; font-size: 50px; color: var(--mark-grey); }
  .byline {
    position: absolute; left: 104px; top: 178px;
    display: flex; gap: 18px; font-size: 16px; color: var(--mark-grey);
  }
  .byline span::before { content: "\2022"; margin-right: 6px; }
</style>
</head>
<body>
  <section class="card card-front" aria-label="Business card front">
    <div class="front-header">
      <span class="brand-name">Tillvanta</span>
    </div>
    <div class="accent-line"></div>
    <div class="info-panel">
      <span class="notch"></span>
      <div class="person">
        <p class="person-name">Surname</p>
        <p class="person-title">Managing Director</p>
        <ul class="contact-list">
          <li><svg viewBox="0 0 14 12"><rect x="1" y="2" width="12" height="8" fill="none" stroke="#f2f2f2" stroke-width="1.3"/><path d="M1 2 L7 7 L13 2" fill="none" stroke="#f2f2f2" stroke-width="1.3"/></svg>first.surname@tillvanta.example</li>
          <li><svg viewBox="0 0 14 12"><path d="M1 4 Q7 -1 13 4 L11 5.5 L9.5 4 L4.5 4 L3 5.5 Z" fill="#f2f2f2"/><rect x="3" y="6" width="8" height="5" rx="1" fill="#f2f2f2"/></svg>+61-427-318-654</li>
        </ul>
      </div>
      <div class="company">
        <p class="company-heading">Offices &amp; Agents:</p>
        <p class="company-cities">Harbourton, Kellmere<br>Ashgrove, Denley, Marrow Bay</p>
        <ul class="contact-list">
          <li><svg viewBox="0 0 14 12"><rect x="4" y="1" width="6" height="4" fill="#f2f2f2"/><rect x="1" y="5" width="12" height="6" rx="1" fill="#f2f2f2"/></svg><span class="sep">:</span>+61-8-7394-2816</li>
          <li><svg viewBox="0 0 14 12"><rect x="1" y="2" width="12" height="8" fill="none" stroke="#f2f2f2" stroke-width="1.3"/><path d="M1 2 L7 7 L13 2" fill="none" stroke="#f2f2f2" stroke-width="1.3"/></svg><span class="sep">:</span>tillvanta@tillvanta.example</li>
          <li><svg viewBox="0 0 14 12"><circle cx="7" cy="6" r="5" fill="none" stroke="#f2f2f2" stroke-width="1.2"/><ellipse cx="7" cy="6" rx="2.2" ry="5" fill="none" stroke="#f2f2f2" stroke-width="1"/><line x1="2" y1="6" x2="12" y2="6" stroke="#f2f2f2" stroke-width="1"/></svg><span class="sep">:</span>www.tillvanta.example</li>
        </ul>
      </div>
    </div>
    <div class="footer-band"></div>
  </section>

  <section class="card card-back" aria-label="Business card back">
    <span class="brand-name">Tillvanta</span>
    <p class="byline"><span>Innovation</span><span>Integrity</span><span>Service</span></p>
  </section>
</body>
</html>
```